Newsletter/Flyer/Advertisement - ("Call for Papers") Design Project

We will be arranging a conference on electronics integration technology in Helsinki, Finland in September 2014 and we would need catchy looking information leaflet to advertise it. We call this a “call for papers” and it is distributed to all potential attendants of the conference. I have attached the plain text part as a MS Word document “1st Call for Papers.docx”. The title format, font etc. can be changed and modified but the 1/2/1 column layout should remain the same and the text should not extend to third page.
There are 5 logos that must be included; the event logo QRVN2014 should be on the front page but the remaining 4 logos (Birchmoor University, OKUW, LDZB, and uTROF) should be placed in the bottom footer of both pages. I have attached the call for papers from the previous QRVN conference (in 2012) as a reference of how it has looked before. However, I would like to make it visually little bit more like the GWYH call for papers, which is also attached. If you can find a little "flavor" perhaps from the theme of the conference (electronics) and/or something local (Helsinki) to make it stand out next to the old QRVN one. I think the theme of electronics is quite universal but I will also attach some photos of Helsinki.
Please do not hesitate to ask for clarifications!
Updates

Target Market(s)

Technical people and academics around the world

Industry/Entity Type

Electronics

Requirements
Must have
• Texh included in the "1st Call for Papers.docx". 5 logos: the QRVN2014 event logo somewhere up in the front; Birchmoor University, OKUW, LDZB, and uTROF logos down in the bottom footer (in this particular order).
Nice to have
• Some local "flavor" from Helsinki and the theme of the conference (microelectronics) present in the appearance.

```html
<!DOCTYPE html>
<html lang="en">
<head>
<meta charset="utf-8">
<title>QRVN2014 Call for Papers – Page 2</title>
<link rel="stylesheet" href="https://fonts.googleapis.com/css2?family=Roboto+Condensed:wght@400;700&display=swap">
<style>
  :root {
    --brand-blue: #1b8fd8;
    --panel-grey: #77787b;
    --ink: #231f20;
    --paper: #ffffff;
    --link: #1b6fc2;
  }
  html, body {
    margin: 0;
    padding: 0;
    overflow: hidden;
    background: var(--paper);
  }
  .page {
    position: relative;
    width: 849px;
    height: 1200px;
    overflow: hidden;
    background: var(--paper);
    font-family: "Roboto Condensed", "Arial Narrow", sans-serif;
    color: var(--ink);
  }
  .page-frame {
    position: absolute;
    inset: 0;
    width: 849px;
    height: 1200px;
  }
  .column {
    position: absolute;
    top: 46px;
    width: 367px;
    font-size: 16.6px;
    line-height: 20.5px;
  }
  .column-left { left: 49px; }
  .column-right { left: 432px; top: 44px; }
  .column p {
    margin: 0;
    text-align: justify;
  }
  .topic-title {
    margin: 0;
    font-size: 16.6px;
    font-weight: 700;
  }
  .section-title {
    margin: 21px 0 2px;
    font-size: 22px;
    line-height: 26px;
    font-weight: 700;
  }
  .column a { color: var(--link); }
  .dates-panel {
    position: absolute;
    left: 432px;
    top: 732px;
    width: 368px;
    height: 183px;
    border-radius: 12px;
    background: var(--brand-blue);
    color: var(--paper);
    box-sizing: border-box;
    padding: 38px 24px 0;
    font-size: 17px;
    line-height: 20.5px;
  }
  .dates-title {
    margin: 0 0 20px;
    font-size: 18px;
    font-weight: 700;
  }
  .dates-row { display: flex; }
  .dates-row span:first-child { width: 193px; }
  .closing-panel {
    position: absolute;
    left: 49px;
    top: 929px;
    width: 751px;
    height: 140px;
    border-radius: 14px;
    background: var(--panel-grey);
    color: var(--paper);
    font-size: 16px;
    line-height: 20px;
  }
  .closing-message {
    margin: 20px 26px 0;
    text-align: center;
  }
  .chair {
    position: absolute;
    top: 82px;
    text-align: center;
    font-size: 15.5px;
    line-height: 19px;
  }
  .chair-general { left: 28px; }
  .chair-executive { left: 330px; }
  .chair-program { right: 28px; }
  .footer-band {
    position: absolute;
    left: 24px;
    top: 1117px;
    width: 825px;
    height: 83px;
    background: var(--brand-blue);
    border-top-left-radius: 10px;
    color: var(--paper);
  }
  .footer-url {
    position: absolute;
    left: 49px;
    top: 28px;
    font-size: 21px;
  }
  .footer-divider {
    position: absolute;
    left: 441px;
    top: 14px;
    width: 2px;
    height: 50px;
    background: var(--paper);
  }
  .partner-row {
    position: absolute;
    left: 520px;
    top: 18px;
    display: flex;
    gap: 12px;
  }
  .partner {
    display: flex;
    flex-direction: column;
    align-items: center;
    width: 64px;
    font-size: 11px;
    line-height: 13px;
    text-align: center;
  }
  .partner-mark {
    width: 26px;
    height: 26px;
    border-radius: 50%;
    background: var(--paper);
    margin-bottom: 4px;
  }
</style>
</head>
<body>
<div class="page">
  <svg class="page-frame" viewBox="0 0 849 1200" aria-hidden="true">
    <path d="M17 40 V1075 a22 22 0 0 0 22 22 H811 a22 22 0 0 0 22 -22 V42 a24 24 0 0 0 -24 -24 H34"
          fill="none" stroke="#1b8fd8" stroke-width="6"/>
    <circle cx="829" cy="190" r="13" fill="#1b8fd8"/>
    <circle cx="829" cy="190" r="18" fill="none" stroke="#1b8fd8" stroke-width="3"/>
    <circle cx="22" cy="911" r="13" fill="#1b8fd8"/>
    <circle cx="22" cy="911" r="18" fill="none" stroke="#1b8fd8" stroke-width="3"/>
  </svg>

  <section class="column column-left">
    <h3 class="topic-title">Materials for Interconnect and Packaging:</h3>
    <p>New materials and processing – e.g. phase change, piezoelectric, self-organizing, and memory materials, dielectric materials, advanced interconnection metallurgies, etc.</p>
    <h3 class="topic-title">MEMS/NEMS packaging:</h3>
    <p>Challenges and solutions in processing, integration, and packaging, new packaging approaches, bonding technologies: wafer bonding, micro-bonding, etc.</p>
    <h3 class="topic-title">Modeling in Electronics:</h3>
    <p>Thermal, mechanical, and electrical modeling and experimental verifications, signal and power integrity, etc.</p>
    <h3 class="topic-title">Optoelectronic Packaging:</h3>
    <p>Fiber optical interconnects, optical sensors, LEDs and other photonic devices, optical chip-scale and heterogeneous integration, lasers, etc.</p>
    <h3 class="topic-title">Power Electronic Packaging:</h3>
    <p>High performance packaging (low RDS(on); high temperature), Si power diode and thyristor devices, wide bandgap power semiconductor devices (e.g. SiC, GaN, GaAs), novel cooling solutions, etc.</p>
    <h3 class="topic-title">Printable electronics:</h3>
    <p>Printed/jetted (transparent) conductors, touch sensors, screens and displays (e.g. OLED), paper electronics, 3D printing, PV, etc.</p>
    <h3 class="topic-title">Reliability:</h3>
    <p>Challenges at different levels of investigations (system, board, package and joint), characterization and test methods, interconnection reliability; characterization, and next generation/novel packaging reliability.</p>
    <h2 class="section-title">Abstract Submission</h2>
    <p>You are invited to submit a 300-500 word abstract that describes the scope, content and key points of your proposed paper. Abstracts must include results and graphics. The official language of all presentations is English. Please visit <a href="#">www.qrvn2014.eu</a> to find more information and to upload your abstract. Submission of abstracts will be opened 1.1.2014 and the abstracts are due 28.2.2014. All abstracts must be submitted electronically at the conference web site.</p>
  </section>

  <section class="column column-right">
    <p>All submitted abstracts will be reviewed by the committee to ensure a high-quality conference. Authors will be notified of paper acceptance with instructions for publication by 18.4.2014.</p>
    <p>If you have any questions, please contact: Julien Marchetti, Program Chair of the 5th QRVN, via email (firstname.lastname@lrn.fr).</p>
    <h2 class="section-title">Publication of Papers</h2>
    <p>All oral and poster presentation papers will be included in the conference proceedings and made available at the OKUW Vaultline Digital Library (vaultline.okuw.org).</p>
    <p>In order to be included in OKUW Vaultline the paper must be original and not previously published, and avoid inclusion of commercial content.</p>
    <h2 class="section-title">Best Paper Awards</h2>
    <p>QRVN will select the best paper presentation. The author(s) will receive a personalized QRVN award and share a check for EUR 1 000.</p>
    <p>QRVN will select the best poster whose author(s) will receive a personalized QRVN award and share a check for EUR 1 000.</p>
    <h2 class="section-title">Professional Development Courses</h2>
    <p>In addition to abstracts for papers we call proposals from individuals interested in teaching educational professional development courses (4 hours) on the topics described in the Call for Papers. Proposal should be submitted to Julien Marchetti, the Program Chair of the 5th QRVN, via email (<a href="#">firstname.lastname@lrn.fr</a>) also by 28.2.2014.</p>
  </section>

  <aside class="dates-panel">
    <h2 class="dates-title">Important Dates:</h2>
    <div class="dates-row"><span>Abstract submission</span><span>: 28.2.2014</span></div>
    <div class="dates-row"><span>Notification of acceptance</span><span>: 18.4.2014</span></div>
    <div class="dates-row"><span>Papers in the final form</span><span>: 20.6.2014</span></div>
  </aside>

  <section class="closing-panel">
    <p class="closing-message">We look forward to welcoming you to the fourth OKUW-LDZB Electronics System-integration Conference QRVN 2014 in Helsinki!</p>
    <div class="chair chair-general">Hanna Virtavaara<br>General Chair</div>
    <div class="chair chair-executive">Oskari Lehtinen<br>Executive Chair</div>
    <div class="chair chair-program">Julien Marchetti<br>Program Chair</div>
  </section>

  <footer class="footer-band">
    <div class="footer-url">www.qrvn2014.eu (http://10.24.118.62)</div>
    <div class="footer-divider"></div>
    <div class="partner-row">
      <div class="partner"><span class="partner-mark"></span>Birchmoor University</div>
      <div class="partner"><span class="partner-mark"></span>OKUW</div>
      <div class="partner"><span class="partner-mark"></span>uTROF</div>
      <div class="partner"><span class="partner-mark"></span>LDZB</div>
    </div>
  </footer>
</div>
</body>
</html>
```